UI/ UX Design for ERP Software

We need a new UX/UI interface for a ERP software for property managers. Our CMMS / ERP solution is made based on responsive design technologies and is coded in PHP.
The overall UX to be similar to Tarn Vexa - easy navigation, intuitive menus.

Industry/Entity Type

Property Management

Number of Pages Required

5+ page

Requirements
Must have
• Round dock buttons
Consistent icons across the application
Enough Spacing between buttons/icons/ menu
Consistent Font
Nice to have
• We would like the UX to allow the users to use the application without /minimum training.
Should not have
• we don't want anything that is classic with respect to UX

```html
<!DOCTYPE html>
<html lang="en">
<head>
<meta charset="UTF-8">
<title>Active Dashboard</title>
<link rel="stylesheet" href="https://fonts.googleapis.com/css2?family=Roboto:wght@400;500&display=swap">
<style>
:root{
  --page:#eaf6fd;
  --header:#003f86;
  --sidebar:#1b86f8;
  --sidebar-active:#0b4d9e;
  --blue:#0a7cf5;
  --cyan:#0db9f4;
  --panel:#f6fafd;
  --plot-light:#f1f1f1;
  --plot-dark:#c9c9c9;
  --grid:#8a8a8a;
  --bar:#74b2f0;
  --legend:#4dbff8;
  --ink:#222;
  --white:#fff;
}
*{margin:0;padding:0;box-sizing:border-box}
html,body{width:1200px;height:643px;overflow:hidden}
body{background:var(--page);font-family:"Roboto",Arial,sans-serif;color:var(--ink);position:relative}
.topbar{position:absolute;left:0;top:0;width:1200px;height:53px;background:var(--header);color:var(--white);display:flex;align-items:center;padding-left:30px;font-size:14px;gap:12px}
.topbar svg{width:20px;height:20px}
.sidebar{position:absolute;left:1031px;top:0;width:169px;height:643px;background:var(--sidebar);border-radius:0 0 0 16px;padding-top:5px}
.nav-item{height:28.7px;display:flex;align-items:center;color:var(--white);font-size:10px;padding-left:11px;gap:17px;width:141px;border-radius:0 10px 10px 0}
.nav-item.active{background:var(--sidebar-active);height:31px;margin-bottom:-2px}
.nav-item svg{width:16px;height:16px;flex:none;fill:var(--white)}
.pill{position:absolute;left:26px;width:162px;border-radius:12px;background:var(--blue);color:var(--white);display:flex;align-items:center;justify-content:center;gap:6px;font-size:10px}
.pill svg{width:11px;height:11px;fill:var(--white)}
.range{top:76px;height:31px}
.dates{top:118px;left:25px;width:165px;height:39px;border-radius:14px}
.stat{position:absolute;color:var(--white);border-radius:14px;display:flex;flex-direction:column;align-items:center;justify-content:center;gap:7px}
.stat .value{font-size:15px}
.stat .label{font-size:10px;display:flex;align-items:center;gap:6px}
.stat svg{width:13px;height:13px}
.cyan{background:var(--cyan)}
.blue{background:var(--blue)}
.small{top:167px;height:64px;width:77px}
.small .value{font-size:14px}
.big{left:25px;width:165px;height:91px;border-radius:18px}
.chart-panel{position:absolute;left:213px;top:77px;width:793px;height:460px;background:var(--panel);border-radius:14px}
.chart-panel svg{position:absolute;left:0;top:0}
.legend{position:absolute;left:25px;top:554px;width:981px;height:71px;background:var(--legend);border-radius:20px;font-size:10px}
.legend-item{position:absolute;display:flex;align-items:center;gap:7px}
.dot{width:15px;height:15px;border-radius:50%;border:1.5px solid var(--white)}
</style>
</head>
<body>
<header class="topbar">
  <svg viewBox="0 0 20 20"><path d="M10 2 1 10h3v8h4v-5h4v5h4v-8h3z" fill="#fff"/></svg>
  <span>Active Dashboard</span>
</header>

<div class="pill range"><svg viewBox="0 0 12 12"><circle cx="6" cy="6" r="6"/><path d="M6 3v3.5h2.5" stroke="#0a7cf5" stroke-width="1.3" fill="none"/></svg>Last 7 Days<svg viewBox="0 0 12 12"><path d="M1 3h10L6 10z"/></svg></div>
<div class="pill dates"><svg viewBox="0 0 12 12"><rect x="0" y="1" width="12" height="11" rx="1"/><rect x="2" y="4" width="8" height="6" fill="#0a7cf5"/></svg>27/12/2020 - 03/01/2021<svg viewBox="0 0 12 12"><path d="M1 3h10L6 10z"/></svg></div>

<div class="stat small cyan" style="left:26px"><span class="value">3</span><span class="label"><svg viewBox="0 0 12 12"><path d="M6 0a4.5 4.5 0 0 0-4.5 4.5C1.5 8 6 12 6 12s4.5-4 4.5-7.5A4.5 4.5 0 0 0 6 0z" fill="#fff"/><circle cx="6" cy="4.5" r="1.6" fill="#0db9f4"/></svg>Propertis</span></div>
<div class="stat small blue" style="left:112px"><span class="value">8</span><span class="label"><svg viewBox="0 0 12 12"><circle cx="6" cy="6" r="6" fill="#fff"/><circle cx="6" cy="5" r="2" fill="#0a7cf5"/><path d="M2.5 10a3.5 3 0 0 1 7 0" fill="#0a7cf5"/></svg>Tenants</span></div>

<div class="stat big cyan" style="top:241px"><span class="value">422,000.00 Sq.ft.</span><span class="label"><svg viewBox="0 0 12 12"><circle cx="6" cy="6" r="5.3" fill="none" stroke="#fff" stroke-width="1.3"/><circle cx="6" cy="6" r="2.5" fill="#fff"/></svg>Total Properties Area</span></div>
<div class="stat big blue" style="top:343px"><span class="value">233,500.00 sq.ft</span><span class="label"><svg viewBox="0 0 12 12"><circle cx="6" cy="6" r="5.3" fill="none" stroke="#fff" stroke-width="1.3"/><circle cx="6" cy="6" r="2.5" fill="#fff"/></svg>Rented Area</span></div>
<div class="stat big cyan" style="top:446px"><span class="value">188,500.00 sq.ft</span><span class="label"><svg viewBox="0 0 12 12"><circle cx="6" cy="6" r="5.3" fill="none" stroke="#fff" stroke-width="1.3"/><circle cx="6" cy="6" r="2.5" fill="#fff"/></svg>Vacancies Area</span></div>

<section class="chart-panel">
  <svg width="793" height="460" viewBox="0 0 793 460" font-family="Roboto, Arial, sans-serif" font-size="10" fill="#222">
    <g transform="translate(66,20)">
      <rect x="0" y="0" width="101" height="397" fill="var(--plot-light)"/>
      <rect x="101" y="0" width="101" height="397" fill="var(--plot-dark)"/>
      <rect x="202" y="0" width="101" height="397" fill="var(--plot-light)"/>
      <rect x="303" y="0" width="101" height="397" fill="var(--plot-dark)"/>
      <rect x="404" y="0" width="101" height="397" fill="var(--plot-light)"/>
      <rect x="505" y="0" width="101" height="397" fill="var(--plot-dark)"/>
      <rect x="606" y="0" width="101" height="397" fill="var(--plot-light)"/>
      <g stroke="var(--grid)" stroke-width="0.7">
        <line x1="0" y1="32" x2="713" y2="32"/>
        <line x1="0" y1="104.5" x2="713" y2="104.5"/>
        <line x1="0" y1="177.5" x2="713" y2="177.5"/>
        <line x1="0" y1="251" x2="713" y2="251"/>
        <line x1="0" y1="324" x2="713" y2="324"/>
        <line x1="0" y1="397" x2="713" y2="397"/>
        <line x1="0" y1="0" x2="0" y2="397"/>
      </g>
      <path d="M335 397V110a5 5 0 0 1 5-5h12a5 5 0 0 1 5 5v287z" fill="var(--bar)"/>
    </g>
    <g class="y-ticks" text-anchor="end">
      <text x="58" y="49">1.25</text>
      <text x="58" y="120">1.00</text>
      <text x="58" y="193">0.75</text>
      <text x="58" y="266">0.50</text>
      <text x="58" y="341">0.25</text>
    </g>
    <text x="34" y="413">0</text>
    <text transform="translate(24,219) rotate(-90)" text-anchor="middle">Number</text>
    <g class="x-ticks" text-anchor="middle">
      <text x="116" y="441">27/12/2020</text>
      <text x="217" y="441">28/12/2020</text>
      <text x="318" y="441">29/12/2020</text>
      <text x="419" y="441">30/12/2020</text>
      <text x="520" y="441">31/12/2020</text>
      <text x="621" y="441">01/01/2020</text>
      <text x="722" y="441">02/01/2020</text>
    </g>
  </svg>
</section>

<section class="legend">
  <div class="legend-item" style="left:41px;top:14px"><span class="dot" style="background:#7ab8f3"></span>Scheduled Maintenance</div>
  <div class="legend-item" style="left:243px;top:12px"><span class="dot" style="background:#8fe08a"></span>Completed Scheduled Maintenance</div>
  <div class="legend-item" style="left:526px;top:14px"><span class="dot" style="background:#f0a36c"></span>Future Scheduled Maintenance</div>
  <div class="legend-item" style="left:795px;top:14px"><span class="dot" style="background:#3d3f45"></span>Scheduled Work Orders</div>
  <div class="legend-item" style="left:41px;top:42px"><span class="dot" style="background:#8f8fe0"></span>Completed Work Orders</div>
  <div class="legend-item" style="left:243px;top:44px"><span class="dot" style="background:#f0557a"></span>Property Inspections in Progress</div>
  <div class="legend-item" style="left:526px;top:44px"><span class="dot" style="background:#e9cf50"></span>Completed Property Inspections</div>
</section>

<nav class="sidebar">
  <div class="nav-item active"><svg viewBox="0 0 16 16"><path d="M8 1 1 8h2v7h4v-4h2v4h4V8h2z"/></svg>Dashboard</div>
  <div class="nav-item"><svg viewBox="0 0 16 16"><circle cx="5" cy="5" r="3"/><circle cx="11" cy="5" r="3"/><path d="M0 14a5 4 0 0 1 10 0zM7 14a5 4 0 0 1 9 0z"/></svg>Customers</div>
  <div class="nav-item"><svg viewBox="0 0 16 16"><path d="M8 1 0 8h2v7h4v-4h4v4h4V8h2z"/></svg>Properties</div>
  <div class="nav-item"><svg viewBox="0 0 16 16"><circle cx="8" cy="8" r="7.5"/><circle cx="8" cy="6.5" r="2.5" fill="#1b86f8"/><path d="M3.5 13a4.5 4 0 0 1 9 0z" fill="#1b86f8"/></svg>Tenants</div>
  <div class="nav-item"><svg viewBox="0 0 16 16"><circle cx="8" cy="5" r="4.5"/><circle cx="8" cy="5" r="2" fill="#1b86f8"/><path d="M2 16a6 5 0 0 1 12 0z"/></svg>Contacts</div>
  <div class="nav-item"><svg viewBox="0 0 16 16"><circle cx="5.5" cy="5.5" r="4.5"/><circle cx="5.5" cy="5.5" r="1.8" fill="#1b86f8"/><circle cx="12" cy="12" r="3.5"/><circle cx="12" cy="12" r="1.3" fill="#1b86f8"/></svg>Contractors</div>
  <div class="nav-item"><svg viewBox="0 0 16 16"><circle cx="3" cy="5" r="2"/><circle cx="8" cy="4" r="2.5"/><circle cx="13" cy="5" r="2"/><path d="M0 13a3 3 0 0 1 6 0zM4 14a4 4 0 0 1 8 0zM10 13a3 3 0 0 1 6 0z"/></svg>Employees</div>
  <div class="nav-item"><svg viewBox="0 0 16 16"><rect x="1" y="2" width="14" height="12" rx="1"/><path d="M3 5h10M3 8h10M3 11h7" stroke="#1b86f8" stroke-width="1.3"/></svg>Prevents,Maintenance</div>
  <div class="nav-item"><svg viewBox="0 0 16 16"><circle cx="6.5" cy="6.5" r="5.5"/><circle cx="6.5" cy="6.5" r="2" fill="#1b86f8"/><circle cx="12.5" cy="12.5" r="3"/></svg>Work Orders</div>
  <div class="nav-item"><svg viewBox="0 0 16 16"><path d="M3 5h10l-1 10H4z"/><path d="M5.5 5a2.5 3 0 0 1 5 0" fill="none" stroke="#fff" stroke-width="1.4"/></svg>Purchase Orders</div>
  <div class="nav-item"><svg viewBox="0 0 16 16"><path d="M2 1h8v6H2z"/><rect x="2" y="1" width="1.5" height="14"/><rect x="2" y="13.5" width="12" height="1.5"/><circle cx="9.5" cy="9" r="3" fill="none" stroke="#fff" stroke-width="1.5"/><path d="M11.5 11l3 3" stroke="#fff" stroke-width="1.8"/></svg>Proerties Inspections</div>
  <div class="nav-item"><svg viewBox="0 0 16 16"><rect x="1" y="8" width="2.5" height="6"/><rect x="5" y="3" width="2.5" height="11"/><rect x="9" y="6" width="2.5" height="8"/><rect x="12.5" y="10" width="2.5" height="4"/><rect x="0" y="14.5" width="16" height="1.3"/></svg>Energy Management</div>
  <div class="nav-item"><svg viewBox="0 0 16 16"><path d="M8 1 15.5 15H.5z"/><rect x="7.2" y="6" width="1.6" height="5" fill="#1b86f8"/><rect x="7.2" y="12" width="1.6" height="1.6" fill="#1b86f8"/></svg>Risk Mangement</div>
  <div class="nav-item"><svg viewBox="0 0 16 16"><rect x="0" y="2" width="3" height="2.5"/><rect x="4.5" y="2" width="11.5" height="2.5"/><rect x="0" y="7" width="3" height="2.5"/><rect x="4.5" y="7" width="11.5" height="2.5"/><rect x="0" y="12" width="3" height="2.5"/><rect x="4.5" y="12" width="11.5" height="2.5"/></svg>Project Management</div>
  <div class="nav-item"><svg viewBox="0 0 16 16"><circle cx="10" cy="6" r="5.5"/><circle cx="6.5" cy="9.5" r="5.5" stroke="#1b86f8" stroke-width="1.2"/><circle cx="6.5" cy="9.5" r="3" fill="#1b86f8"/></svg>Finacial-Budgeting</div>
  <div class="nav-item"><svg viewBox="0 0 16 16"><path d="M1 2h14v9H6l-4 4v-4H1z"/><circle cx="5" cy="6.5" r="1" fill="#1b86f8"/><circle cx="8" cy="6.5" r="1" fill="#1b86f8"/><circle cx="11" cy="6.5" r="1" fill="#1b86f8"/></svg>Tenants Requests</div>
  <div class="nav-item"><svg viewBox="0 0 16 16"><rect x="2" y="1" width="12" height="14" rx="1"/><path d="M5 5h6M5 8h6M5 11h4" stroke="#1b86f8" stroke-width="1.3"/></svg>Repors</div>
  <div class="nav-item"><svg viewBox="0 0 16 16"><path d="M0 12 5 6l4 4 6-7" fill="none" stroke="#fff" stroke-width="1.8"/><rect x="0" y="14" width="16" height="1.5"/></svg>Visual Reports</div>
  <div class="nav-item"><svg viewBox="0 0 16 16"><rect x="0" y="4" width="12" height="11"/><rect x="3" y="1" width="12" height="11" stroke="#1b86f8" stroke-width="1"/></svg>Files</div>
  <div class="nav-item"><svg viewBox="0 0 16 16"><path d="M2 0h8l4 4v12H2z"/><path d="M5 8h6M5 11h6" stroke="#1b86f8" stroke-width="1.3"/></svg>pages</div>
  <div class="nav-item"><svg viewBox="0 0 16 16"><circle cx="6" cy="10" r="5"/><circle cx="6" cy="10" r="2" fill="#1b86f8"/><circle cx="12.5" cy="3.5" r="3"/><circle cx="12.5" cy="3.5" r="1.1" fill="#1b86f8"/></svg>Configurations</div>
  <div class="nav-item"><svg viewBox="0 0 16 16"><path d="M2 2l12 12M14 2 2 14" stroke="#fff" stroke-width="2.4"/><circle cx="3" cy="3" r="2.5"/><circle cx="13" cy="13" r="2.5"/></svg>Settings</div>
</nav>
</body>
</html>
```